Small IT consulting firm needs a new web site

Quellmark Systems, LLC is a company based out of Arizona with national presence. We work on both national, multinational, and international projects. We are Brantova Partners. Heavy experience and work with Nodewell Control Suite, Velquo, Trellin 820 . We offer Architecture, Design, Development, and implementation services. We have a specialty in Trellin 820 migrations and implementations. We also have a specialized practice in Program and Project Management. The design message should foster a feeling of partnership and experience. Attached is my logo.
Industry/Entity Type
It Company
Coding
Coded - Design and coding required
Number of Pages Required
5+ page
Look and feel

```html
<!DOCTYPE html>
<html lang="en">
<head>
<meta charset="utf-8">
<title>Quellmark Systems, LLC</title>
<link rel="stylesheet" href="https://fonts.googleapis.com/css2?family=Source+Sans+3:ital,wght@0,400;0,600;0,700;1,400;1,600&display=swap">
<style>
:root{
  --red:#c8202f;
  --red-dark:#a81824;
  --ink:#3a3a3a;
  --muted:#6b6b6b;
  --line:#dcdcdc;
  --soft:#f5f5f5;
  --white:#ffffff;
  --footer:#2e2e2e;
  --footer-deep:#232323;
  --footer-text:#e4e4e4;
}
*{box-sizing:border-box;margin:0;padding:0}
html,body{width:1200px;height:2257px;overflow:hidden;background:var(--white)}
body{font-family:"Source Sans 3",Arial,sans-serif;color:var(--ink)}
.page{position:relative;width:1200px;height:2257px;overflow:hidden}
.abs{position:absolute}

/* header */
.site-header{left:0;top:0;width:1200px;height:96px;background:var(--white);border-bottom:3px solid #e6e6e6}
.brand{left:75px;top:24px;display:flex;align-items:center;gap:10px}
.brand-mark{width:34px;height:34px;background:var(--red)}
.brand-name{font-size:22px;font-weight:700;color:var(--red);line-height:1}
.divider{width:2px;background:#cfcfcf}
.nav a{position:absolute;font-size:14px;color:var(--muted);text-decoration:none;top:40px}
.nav .active{left:398px;top:26px;width:86px;height:42px;background:var(--red);color:var(--white);border-radius:3px;text-align:center;line-height:42px}
.social{display:flex;gap:8px}
.social span{width:32px;height:32px;border-radius:50%;background:var(--red);display:block}
.header-phone{left:965px;top:54px;font-size:21px;color:#7a7a7a}

/* hero */
.hero{left:0;top:96px;width:1200px;height:483px;background:var(--white)}
.hero-visual{left:591px;top:5px;width:529px;height:475px;border-radius:40% 40% 10% 10%;background:radial-gradient(ellipse at 55% 35%,#e9f2f8 0%,#7cc3e6 38%,#d8dee3 60%,#ffffff 78%)}
.hero-title{left:73px;top:200px;font-size:45px;font-weight:600;color:var(--red);line-height:1}
.hero-sub{left:73px;top:262px;font-size:47px;font-weight:600;color:var(--ink);line-height:1}
.hero-text{left:75px;top:333px;width:580px;font-size:21px;line-height:27px;color:var(--ink)}
.btn-red{background:var(--red);color:var(--white);border-radius:3px;text-align:center}
.hero-cta{left:75px;top:456px;width:188px;height:62px;line-height:62px;font-size:24px}
.slider-bar{left:0;top:579px;width:1200px;height:34px;background:#ececec;display:flex;justify-content:center;align-items:center;gap:3px}
.slider-bar i{width:15px;height:15px;border-radius:50%;background:#222;border:3px solid #ececec;box-shadow:0 0 0 1px #222}
.slider-bar i.on{background:#1f5f9e}

/* welcome */
.welcome{left:0;top:613px;width:1200px;height:280px;background:var(--red);color:var(--white);text-align:center}
.welcome h2{position:absolute;left:0;top:46px;width:1200px;font-size:28px;font-style:italic;font-weight:400}
.welcome p{position:absolute;left:171px;top:100px;width:858px;font-size:17px;line-height:23px}
.btn-white{background:var(--white);color:var(--ink);border-radius:3px;text-align:center}
.welcome .btn-white{position:absolute;left:534px;top:182px;width:132px;height:45px;line-height:45px;font-size:18px}

/* sections */
.section-title{width:1200px;left:0;text-align:center;font-size:26px;font-style:italic;color:var(--ink)}
.services{left:0;top:893px;width:1200px;height:472px;background:var(--soft)}
.service-card{top:81px;width:254px;height:361px;background:var(--white);border:1px solid var(--line)}
.service-photo{width:252px;height:152px}
.service-icon{position:absolute;left:104px;top:131px;width:46px;height:46px;border-radius:50%;background:var(--white);border:2px solid #eee;display:flex;align-items:center;justify-content:center}
.service-card h3{position:absolute;top:214px;width:100%;text-align:center;font-size:15px;font-weight:400}
.service-card p{position:absolute;top:243px;left:12px;width:228px;text-align:center;font-size:10.5px;line-height:14px}
.service-card .btn-red{position:absolute;left:92px;top:302px;width:70px;height:38px;line-height:38px;font-size:14px}

.testimonials{left:0;top:1365px;width:1200px;height:331px;background:var(--white)}
.quote-card{top:96px;width:342px;height:196px;border:1px solid var(--line);background:var(--white)}
.avatar{position:absolute;left:22px;top:10px;width:52px;height:52px;border-radius:50%;background:linear-gradient(#e7d2c2,#b89a86)}
.quote-card h4{position:absolute;left:86px;top:20px;font-size:15px;font-weight:600}
.quote-card .place{position:absolute;left:86px;top:40px;font-size:10px;font-style:italic;color:var(--red)}
.quote-card hr{position:absolute;left:22px;top:74px;width:300px;border:0;border-top:1px solid var(--line)}
.quote-card p{position:absolute;left:22px;top:100px;width:300px;font-size:13px;line-height:23px;font-style:italic;color:var(--muted)}

.partners{left:0;top:1696px;width:1200px;height:174px;background:var(--soft)}
.partner-row{left:0;top:80px;width:1200px;display:flex;justify-content:center;align-items:center;gap:56px}
.partner{display:flex;align-items:center;gap:10px;font-size:30px;font-weight:600}
.partner .mark{width:30px;height:30px}

/* footer */
.site-footer{left:0;top:1870px;width:1200px;height:346px;background:var(--footer);color:var(--footer-text)}
.footer-col h5{font-size:20px;font-weight:400;font-style:italic;color:var(--white);padding-bottom:4px;border-bottom:1px solid #444;width:300px}
.footer-col ul{list-style:none;margin-top:18px}
.footer-col li{font-size:14px;font-style:italic;height:30px;display:flex;align-items:center;gap:12px}
.footer-col li::before{content:"";width:9px;height:9px;border:1px solid #777;transform:rotate(45deg);margin-left:4px}
.footer-phone{left:73px;top:250px;font-size:15px;font-style:italic;font-weight:600}
.footer-phone b{font-size:26px;margin-left:22px}
.footer-follow{left:73px;top:290px;font-size:15px;font-style:italic;font-weight:600;display:flex;align-items:center;gap:8px}
.footer-follow span{width:24px;height:24px;border-radius:50%;background:var(--white);display:inline-block}
.field{left:829px;width:294px;border:1px solid #9a9a9a;border-radius:3px;font-size:13px;color:#bbb;padding:9px 12px}
.send{left:918px;top:288px;width:106px;height:28px;line-height:28px;background:var(--white);color:#222;text-align:center;font-size:14px;font-weight:600}
.copyright{left:0;top:2216px;width:1200px;height:41px;background:var(--footer-deep);color:#bbb;font-size:11px;text-align:center;line-height:41px}
</style>
</head>
<body>
<div class="page">

  <header class="site-header abs">
    <div class="brand abs"><span class="brand-mark"></span><span class="brand-name">Quellmark Systems, LLC</span></div>
    <div class="divider abs" style="left:288px;top:10px;height:74px"></div>
    <nav class="nav">
      <a class="active" href="#">Home</a>
      <a href="#" style="left:522px">About</a>
      <a href="#" style="left:616px">Services</a>
      <a href="#" style="left:713px">Contact Us</a>
    </nav>
    <div class="divider abs" style="left:915px;top:10px;height:74px"></div>
    <div class="social abs" style="left:964px;top:20px"><span></span><span></span><span></span><span></span></div>
    <div class="header-phone abs">+1-888-555-0142</div>
  </header>

  <section class="hero abs">
    <div class="hero-visual abs" role="img" aria-label="Globe surrounded by a ring of networked laptops"></div>
  </section>
  <h1 class="hero-title abs">Quellmark Systems, LLC</h1>
  <div class="hero-sub abs">Quality and Personal Service</div>
  <p class="hero-text abs">Lorem Ipsum is simply dummy text of the printing and typesetting industry. Lorem Ipsum has been the industry's standard dummy text ever since the 1500s.</p>
  <div class="hero-cta btn-red abs">Get in Touch</div>
  <div class="slider-bar abs"><i class="on"></i><i></i><i></i></div>

  <section class="welcome abs">
    <h2>“Welcome”</h2>
    <p>Lorem Ipsum is simply dummy text of the printing and typesetting industry. Lorem Ipsum has been the industry's standard dummy text ever since the 1500s.</p>
    <div class="btn-white">Read More</div>
  </section>

  <section class="services abs">
    <h2 class="section-title abs" style="top:22px">Our Services</h2>

    <article class="service-card abs" style="left:73px">
      <div class="service-photo" role="img" aria-label="Team reviewing plans around a table" style="background:linear-gradient(135deg,#3a3f4a,#c9ccd2)"></div>
      <div class="service-icon"><svg width="22" height="22" viewBox="0 0 22 22"><g fill="#ccc"><rect x="3" y="4" width="10" height="3"/><rect x="7" y="10" width="12" height="3"/><rect x="3" y="16" width="8" height="3"/></g></svg></div>
      <h3>Project Management</h3>
      <p>Lorem Ipsum is simply dummy text of the printing and typesetting industry. Lorem Ipsum has been the industry's standard dummy text</p>
      <div class="btn-red">More</div>
    </article>

    <article class="service-card abs" style="left:339px">
      <div class="service-photo" role="img" aria-label="House model resting on blueprints" style="background:linear-gradient(135deg,#6f8ea8,#dfe8ef)"></div>
      <div class="service-icon"><svg width="22" height="22" viewBox="0 0 22 22"><circle cx="11" cy="11" r="8" fill="none" stroke="#ccc" stroke-width="3"/><circle cx="11" cy="11" r="3" fill="#ccc"/></svg></div>
      <h3>Technical Architecture</h3>
      <p>Lorem Ipsum is simply dummy text of the printing and typesetting industry. Lorem Ipsum has been the industry's standard dummy text</p>
      <div class="btn-red">More</div>
    </article>

    <article class="service-card abs" style="left:605px">
      <div class="service-photo" role="img" aria-label="Mechanical gears with blue wireframe overlay" style="background:linear-gradient(135deg,#3b4450,#1e5fd0)"></div>
      <div class="service-icon"><svg width="24" height="22" viewBox="0 0 24 22"><path d="M3 17a9 9 0 0 1 18 0z" fill="#ccc"/><rect x="1" y="17" width="22" height="3" fill="#ccc"/></svg></div>
      <h3>Engineering</h3>
      <p>Lorem Ipsum is simply dummy text of the printing and typesetting industry. Lorem Ipsum has been the industry's standard dummy text</p>
      <div class="btn-red">More</div>
    </article>

    <article class="service-card abs" style="left:871px">
      <div class="service-photo" role="img" aria-label="Hand selecting a person from a network of contacts" style="background:linear-gradient(135deg,#4a78b4,#1c2f55)"></div>
      <div class="service-icon"><svg width="24" height="22" viewBox="0 0 24 22"><g fill="#ccc"><circle cx="8" cy="7" r="4"/><circle cx="16" cy="7" r="4"/><path d="M1 19a7 6 0 0 1 14 0z"/><path d="M9 19a7 6 0 0 1 14 0z"/></g></svg></div>
      <h3>Staff Augmentation</h3>
      <p>Lorem Ipsum is simply dummy text of the printing and typesetting industry. Lorem Ipsum has been the industry's standard dummy text</p>
      <div class="btn-red">More</div>
    </article>
  </section>

  <section class="testimonials abs">
    <h2 class="section-title abs" style="top:28px">Testimonials</h2>
    <article class="quote-card abs" style="left:73px">
      <div class="avatar" role="img" aria-label="Client portrait"></div>
      <h4>Ardent Loop Group</h4><div class="place">America</div><hr>
      <p>“ Lorem Ipsum is simply dummy text of the printing and typesetting industry. Lorem Ipsum has been the industry's standard dummy text... ”</p>
    </article>
    <article class="quote-card abs" style="left:428px">
      <div class="avatar" role="img" aria-label="Client portrait"></div>
      <h4>Corvane Trust</h4><div class="place">America</div><hr>
      <p>“ Lorem Ipsum is simply dummy text of the printing and typesetting industry. Lorem Ipsum has been the industry's standard dummy text... ”</p>
    </article>
    <article class="quote-card abs" style="left:781px">
      <div class="avatar" role="img" aria-label="Client portrait"></div>
      <h4>Halberd Controls</h4><div class="place">America</div><hr>
      <p>“ Lorem Ipsum is simply dummy text of the printing and typesetting industry. Lorem Ipsum has been the industry's standard dummy text... ”</p>
    </article>
  </section>

  <section class="partners abs">
    <h2 class="section-title abs" style="top:16px">Partners</h2>
    <div class="partner-row abs">
      <div class="partner" style="font-size:24px;color:#333"><span class="mark" style="background:#9aa3ad;border-radius:50%"></span>Nodewell Control Suite</div>
      <div class="partner" style="color:#1a73d9"><span class="mark" style="background:#1a73d9;border-radius:50%"></span>Velquo</div>
      <div class="partner" style="color:#e0461b"><span class="mark" style="background:#e0461b"></span>Trellin 820</div>
      <div class="partner" style="color:#5b8ee8">Brantova</div>
    </div>
  </section>

  <footer class="site-footer abs">
    <div class="footer-col abs" style="left:73px;top:36px">
      <h5 style="width:300px">Menu</h5>
      <ul><li>Home</li><li>About Us</li><li>Service</li><li>Contact Us</li></ul>
    </div>
    <div class="abs" style="left:73px;top:226px;width:300px;border-top:1px solid #444"></div>
    <div class="footer-phone abs">Phone # &nbsp;: <b>1-888-555-0142</b></div>
    <div class="footer-follow abs">Follow Us : &nbsp;<span></span><span></span><span></span><span></span></div>

    <div class="footer-col abs" style="left:450px;top:36px">
      <h5>Quick Links</h5>
      <ul><li>Portfolio</li><li>program</li><li>project management</li><li>Technical Architecture</li><li>Design</li><li>Engineering</li><li>Staff Augmentation</li></ul>
    </div>

    <div class="footer-col abs" style="left:829px;top:36px">
      <h5 style="width:294px">Get in Touch</h5>
    </div>
    <div class="field abs" style="top:77px;height:40px">Name</div>
    <div class="field abs" style="top:126px;height:39px">E-mail</div>
    <div class="field abs" style="top:176px;height:95px">Message</div>
    <div class="send abs">Send</div>
  </footer>
  <div class="copyright abs">Quellmark Systems, LLC © 2015 All Rights Reserved</div>

</div>
</body>
</html>
```